Flyer for the Harvest of lanterns conference

Flyer design for an annual international conference called "VELMARK 2017". This is a conference for young adults, so we hope to produce a design that is both professional and appealing to young people in general

We'd like the flyer to showcase the conference brand logo, and clearly highlight the key information to people who will read it.

Target Market(s)

Young people, young adults

Industry/Entity Type

Religious

Font styles to use
Sans Serif

Colors

Designer to choose colors to be used in the design.

Requirements
Must have
• - Should be only one page (Vertical or Horizontal).
• - the VELMAK logo and all the information found in the attached text file. This includes: Main topic: Your sons and daughters shall prophesy,
• Dates and time, location, contact information and everything that is in the attached text file.
Nice to have
• It would be nice to see samples where the white logo is used and another where the black one is used.
Should not have
• This is NOT a folded flyer, we will be sticking it on doors and public places. And we will be printing large simple to put on walls. So only one page with few words like an add (the words are in the attached file)

```html
<!DOCTYPE html>
<html lang="en">
<head>
<meta charset="utf-8">
<title>VELMARK 2017 – Harvest of lanterns conference</title>
<link href="https://fonts.googleapis.com/css2?family=Lato:wght@400;700&family=Oswald:wght@400;500;700&display=swap" rel="stylesheet">
<style>
  :root {
    --orange: #f07a12;
    --orange-deep: #e2600a;
    --orange-light: #f6951f;
    --ink: #2b2b2b;
    --heading-grey: #474747;
    --avatar-grey: #9a9a9a;
    --page: #ffffff;
    --backdrop: #e9e7e4;
  }
  html, body {
    margin: 0;
    width: 1200px;
    height: 1200px;
    overflow: hidden;
    background: var(--backdrop);
  }
  .flyer {
    position: absolute;
    left: 197px;
    top: 30px;
    width: 944px;
    height: 1336px;
    background: var(--page);
    transform: scale(0.8533);
    transform-origin: top left;
    box-shadow: 0 6px 24px rgba(0,0,0,.18);
    overflow: hidden;
    font-family: 'Lato', sans-serif;
    color: var(--ink);
  }
  .flyer-shapes { position: absolute; inset: 0; }
  .brand {
    position: absolute;
    left: 402px;
    top: 36px;
    transform: translateX(-50%);
    display: flex;
    flex-direction: column;
    align-items: center;
    gap: 10px;
  }
  .brand-dot {
    width: 96px; height: 96px;
    border-radius: 50%;
    background: var(--orange);
  }
  .brand-name {
    font-family: 'Oswald', sans-serif;
    font-weight: 500;
    font-size: 30px;
    letter-spacing: 3px;
    color: var(--ink);
  }
  .title, .subtitle {
    position: absolute;
    white-space: nowrap;
    color: #fff;
    transform: translate(-50%, -50%) rotate(-15.5deg);
    margin: 0;
  }
  .title {
    left: 462px; top: 594px;
    font-family: 'Oswald', sans-serif;
    font-weight: 700;
    font-size: 80px;
    line-height: 1;
    letter-spacing: 1px;
  }
  .subtitle {
    left: 482px; top: 672px;
    font-family: 'Lato', sans-serif;
    font-weight: 400;
    font-size: 44px;
    line-height: 1;
    letter-spacing: 1px;
  }
  .speakers {
    position: absolute;
    left: 34px;
    top: 866px;
  }
  .speakers-label {
    font-size: 32px;
    margin: 0 0 18px;
    font-weight: 400;
  }
  .speaker-list { list-style: none; margin: 0; padding: 0; }
  .speaker {
    display: flex;
    align-items: center;
    height: 74.5px;
    font-size: 23px;
  }
  .speaker-avatar {
    width: 62px; height: 62px;
    border-radius: 50%;
    background: var(--avatar-grey);
    box-shadow: inset 0 0 0 4px #c4c4c4;
    margin-right: 20px;
    flex: none;
  }
  .theme {
    position: absolute;
    left: 538px;
    top: 782px;
    margin: 0;
    font-family: 'Oswald', sans-serif;
    font-weight: 500;
    font-size: 33px;
    line-height: 54px;
    color: var(--heading-grey);
    letter-spacing: -0.3px;
    white-space: nowrap;
  }
  .event-detail {
    position: absolute;
    left: 538px;
    display: flex;
    align-items: center;
    gap: 12px;
    font-family: 'Oswald', sans-serif;
    font-size: 22px;
    color: var(--heading-grey);
    font-weight: 500;
    white-space: nowrap;
  }
  .event-detail .accent { color: var(--orange); }
  .event-date { top: 918px; }
  .event-time { top: 960px; }
  .venue {
    position: absolute;
    left: 538px;
    font-size: 15px;
    line-height: 19px;
    display: flex;
    gap: 14px;
    white-space: nowrap;
  }
  .venue-address { top: 1028px; }
  .venue-room { top: 1104px; align-items: center; }
  .contact {
    position: absolute;
    right: 34px;
    top: 1172px;
    text-align: right;
    color: #fff;
  }
  .contact-title { font-weight: 700; font-size: 26px; margin: 0 0 10px; }
  .contact-line {
    display: flex;
    justify-content: flex-end;
    align-items: center;
    gap: 12px;
    font-size: 20px;
    height: 31px;
  }
  .contact-web { letter-spacing: 3px; }
</style>
</head>
<body>
  <main class="flyer">
    <svg class="flyer-shapes" width="944" height="1336" viewBox="0 0 944 1336">
      <defs>
        <linearGradient id="band" x1="0" y1="1" x2="1" y2="0">
          <stop offset="0" stop-color="#e2600a"/>
          <stop offset="1" stop-color="#f6921e"/>
        </linearGradient>
        <linearGradient id="photoTone" x1="0" y1="0" x2="1" y2="1">
          <stop offset="0" stop-color="#f3ebe0"/>
          <stop offset="0.55" stop-color="#d9b793"/>
          <stop offset="1" stop-color="#b77a55"/>
        </linearGradient>
        <linearGradient id="column" x1="0" y1="0" x2="1" y2="0">
          <stop offset="0" stop-color="#ffffff"/>
          <stop offset="1" stop-color="#f1f1f1"/>
        </linearGradient>
      </defs>
      <rect class="column-shade" x="0" y="760" width="482" height="576" fill="url(#column)"/>
      <path class="side-fold" d="M944 628 L820 660 L944 790 Z" fill="#ececec"/>
      <path class="hero-photo" role="img" aria-label="Photo: young adults holding hands in prayer around a shared dinner table"
            d="M0 0 H944 V338 C700 470 420 560 250 600 C150 624 60 585 0 520 Z" fill="url(#photoTone)"/>
      <path class="title-band" d="M0 520 C60 585 150 624 250 600 C420 560 700 470 944 338 V628 L330 795 C200 835 100 850 0 828 Z" fill="url(#band)"/>
      <path class="footer-band" d="M200 1336 L720 1158 C800 1128 880 1130 944 1150 V1336 Z" fill="url(#band)"/>
    </svg>

    <div class="brand">
      <span class="brand-dot"></span>
      <span class="brand-name">VELMAK</span>
    </div>

    <h1 class="title">VELMARK 2017</h1>
    <p class="subtitle">Harvest of lanterns conference</p>

    <section class="speakers">
      <h2 class="speakers-label">Speakers:</h2>
      <ul class="speaker-list">
        <li class="speaker"><span class="speaker-avatar"></span>Prophet Tobias Arnvale</li>
        <li class="speaker"><span class="speaker-avatar"></span>Bishop Marcus Telundo</li>
        <li class="speaker"><span class="speaker-avatar"></span>Prophet Samuel Rhee Kalondo</li>
        <li class="speaker"><span class="speaker-avatar"></span>Prophet Elian Sorevo</li>
        <li class="speaker"><span class="speaker-avatar"></span>Prophet Jonas Melenga</li>
      </ul>
    </section>

    <h2 class="theme">YOUR SONS AND DAUGHTERS<br>SHALL PROPHESY</h2>

    <div class="event-detail event-date">
      <svg width="22" height="20" viewBox="0 0 22 20"><rect x="1" y="3" width="20" height="16" fill="none" stroke="#666" stroke-width="1.5"/><line x1="1" y1="7" x2="21" y2="7" stroke="#666" stroke-width="1.5"/><line x1="6" y1="1" x2="6" y2="5" stroke="#666" stroke-width="1.5"/><line x1="16" y1="1" x2="16" y2="5" stroke="#666" stroke-width="1.5"/></svg>
      <span><span class="accent">September</span> 1st, 2nd and 3rd 2017</span>
    </div>
    <div class="event-detail event-time">
      <svg width="22" height="22" viewBox="0 0 22 22"><circle cx="11" cy="11" r="9.5" fill="none" stroke="#666" stroke-width="1.5"/><path d="M11 5 V11 L15 14" fill="none" stroke="#666" stroke-width="1.5"/></svg>
      <span><span class="accent">Start Time:</span> 6:00PM</span>
    </div>

    <div class="venue venue-address">
      <svg width="22" height="30" viewBox="0 0 22 30"><path d="M11 1 C5 1 1 5.5 1 11 C1 18 11 29 11 29 C11 29 21 18 21 11 C21 5.5 17 1 11 1 Z" fill="#f07a12"/><circle cx="11" cy="11" r="4" fill="#fff"/></svg>
      <span>Northgate Harbor Inn<br>412 Cedar Avenue<br>Westbrook Falls, ME 04999 United States</span>
    </div>
    <div class="venue venue-room">
      <svg width="24" height="20" viewBox="0 0 24 20"><path d="M12 1 L23 10 H20 V19 H14 V13 H10 V19 H4 V10 H1 Z" fill="#f07a12"/></svg>
      <span>Room: Fernlight Ballroom</span>
    </div>

    <section class="contact">
      <h2 class="contact-title">Contact Info:</h2>
      <div class="contact-line"><span>+1 (555) 018 2244</span>
        <svg width="18" height="18" viewBox="0 0 18 18"><path d="M4 1 L7 5 L5 7 C6 10 8 12 11 13 L13 11 L17 14 L15 17 C8 17 1 10 1 3 Z" fill="none" stroke="#fff" stroke-width="1.4"/></svg></div>
      <div class="contact-line"><span>hello@cedargrove.org</span>
        <svg width="20" height="14" viewBox="0 0 20 14"><rect x="1" y="1" width="18" height="12" fill="none" stroke="#fff" stroke-width="1.4"/><path d="M1 1 L10 8 L19 1" fill="none" stroke="#fff" stroke-width="1.4"/></svg></div>
      <div class="contact-line contact-web"><span>www.velmarkfest.org</span>
        <svg width="19" height="19" viewBox="0 0 20 20"><circle cx="10" cy="10" r="9" fill="none" stroke="#fff" stroke-width="1.4"/><ellipse cx="10" cy="10" rx="4" ry="9" fill="none" stroke="#fff" stroke-width="1.4"/><line x1="1" y1="10" x2="19" y2="10" stroke="#fff" stroke-width="1.4"/></svg></div>
    </section>
  </main>
</body>
</html>
```